依頼詳細
■デザインのイメージ
・通りがかりでもパッと目を引くようなデザインでお願いします。
・ノマドカフェとバナナジュースのお店であることがパッと見てわかるようなデザインでお願いいたします。
・店内で使用しているメニュー表やのぼりの旗などのデザインと統一性を持たせつつも、タペストリーはシンプルに仕上げられたらと思っております。
・メインカラーが黄色で、サブカラーは #5ABEC2くらいの水色でお願いします。
・参考になりそうなタペストリー(ワイン食堂のお店とバナナジュースのお店)も添付させていただいております。

■ターゲット層
フリーランス、大学生(テイクアウトで高校生も想定)、その他
記載項目
・デザインに使用するロゴは縦と横(白縁ありとなし)がございますので、添付しております。
・参考にしていただきたい、当店のメニュー表やのぼりの旗のデザインも添付しております。
・またInstagram( https://www.fotolane.net/kumo.mikan/ )でお店の雰囲気も参考にしていただけますと幸いです。
・Instagramの画像は自由にご使用くださいませ。実際にご依頼となりましたら、元データをお送りさせていただくことが可能です。
希望イメージ
シンプル 複雑
単色 カラフル
暗い 明るい
日常 高級
遊び心 厳粛
未来的 伝統的
女性的 男性的
希望する色
黄・オレンジ系、水色系
納品ファイル
• 高解像度JPG (.jpg)
• イラストレーター形式 (.ai)
• PNG形式 (.png)
補足説明
■ 選んだ理由

外観に飾るタペストリーということで、パッと目を引くデザインがいいなと思っていたのですが、キャラクターを大きくデザインするという当方では思いつかないデザインがとても魅力的でした!

■ 提案者全員のお礼・コメント

この度は、たくさんの素敵なデザインをご提案いただきまして、誠にありがとうございました!

```html
<!DOCTYPE html>
<html lang="ja">
<head>
<meta charset="utf-8">
<title>ごろごろバナナ タペストリー</title>
<link rel="stylesheet" href="https://fonts.googleapis.com/css2?family=M+PLUS+Rounded+1c:wght@500;800;900&display=swap">
<style>
  :root {
    --teal: #5abec2;
    --yellow: #ffe500;
    --white: #ffffff;
    --ink: #2b2b2b;
  }
  html, body { margin: 0; padding: 0; overflow: hidden; }
  body { width: 779px; height: 1200px; }
  .tapestry {
    position: relative;
    width: 779px; height: 1200px;
    background: var(--teal);
    font-family: "M PLUS Rounded 1c", sans-serif;
    overflow: hidden;
  }
  .tagline, .headline, .info {
    position: absolute; left: 0; width: 100%; margin: 0;
    text-align: center; white-space: nowrap; line-height: 1;
  }
  .tagline {
    top: 92px;
    color: var(--yellow); font-weight: 900; font-size: 60px; letter-spacing: 0;
  }
  .headline {
    top: 192px;
    color: var(--white); font-weight: 900; font-size: 96px; letter-spacing: 2px;
  }
  .emblem {
    position: absolute; left: 183px; top: 318px;
    width: 412px; height: 412px; border-radius: 50%;
    background: var(--yellow);
  }
  .mascot {
    position: absolute; left: 106px; top: 36px;
    width: 200px; height: 230px; border-radius: 90px 90px 60px 60px;
    background: linear-gradient(180deg, #b07a45, #f2cf6a);
  }
  .brand {
    position: absolute; left: 0; top: 276px; width: 100%;
    text-align: center; color: var(--ink); white-space: nowrap;
  }
  .brand-name { display: block; font-weight: 900; font-size: 50px; line-height: 1; }
  .brand-roman { display: block; font-weight: 800; font-size: 20px; margin-top: 8px; }
  .amenities { position: absolute; left: 0; top: 790px; width: 100%; height: 240px; }
  .laptop { position: absolute; left: 112px; top: 50px; }
  .cable { position: absolute; left: 340px; top: 95px; }
  .drink {
    position: absolute; left: 520px; top: 10px;
    width: 150px; height: 215px;
    background: linear-gradient(180deg, #eef3f2, #f7f1e0);
    clip-path: polygon(0 12%, 100% 12%, 88% 100%, 12% 100%);
  }
  .info { color: var(--white); font-weight: 800; }
  .info-power { top: 1064px; font-size: 40px; }
  .info-offer { top: 1120px; font-size: 44px; }
</style>
</head>
<body>
<main class="tapestry">
  <p class="tagline">バナナジュースが飲める</p>
  <h1 class="headline">ノマド・カフェ</h1>

  <div class="emblem">
    <div class="mascot" role="img" aria-label="バナナと電源プラグを持つ猿のキャラクターイラスト"></div>
    <div class="brand">
      <span class="brand-name">ごろごろバナナ</span>
      <span class="brand-roman">Gorogoro Banana</span>
    </div>
  </div>

  <div class="amenities">
    <svg class="laptop" width="210" height="110" viewBox="0 0 210 110" aria-label="Wi-Fi無料のノートパソコン">
      <rect x="22" y="4" width="166" height="90" rx="6" fill="var(--ink)"/>
      <rect x="32" y="13" width="146" height="72" fill="var(--white)"/>
      <rect x="0" y="94" width="210" height="12" rx="4" fill="var(--ink)"/>
      <rect x="70" y="24" width="70" height="32" rx="8" fill="none" stroke="var(--ink)" stroke-width="4"/>
      <text x="105" y="48" text-anchor="middle" font-family="M PLUS Rounded 1c, sans-serif" font-weight="800" font-size="20" fill="var(--ink)">WiFi</text>
      <text x="105" y="76" text-anchor="middle" font-family="M PLUS Rounded 1c, sans-serif" font-weight="800" font-size="16" fill="var(--ink)">FREE</text>
    </svg>
    <svg class="cable" width="140" height="70" viewBox="0 0 140 70" aria-label="電源プラグ">
      <path d="M6 20 C30 -4 40 60 70 40 C85 30 90 34 96 34" fill="none" stroke="var(--ink)" stroke-width="6" stroke-linecap="round"/>
      <rect x="94" y="22" width="26" height="26" rx="4" fill="var(--ink)"/>
      <rect x="118" y="26" width="18" height="5" fill="var(--ink)"/>
      <rect x="118" y="39" width="18" height="5" fill="var(--ink)"/>
    </svg>
    <div class="drink" role="img" aria-label="ストロー付きカップのバナナジュース写真"></div>
  </div>

  <p class="info info-power">電源 &amp; Wi-Fi完備</p>
  <p class="info info-offer">1日980円でバナナジュース一杯無料</p>
</main>
</body>
</html>
```